Dental Practice Website design

Design a new website for Brindle Dental Practice.
Design should be warm, neutral in colour, with some small amount of bright colour if needed but kept to a minimum. Website should look professional, high end. Home page should be easy to navigate and simple for patients to be able to book online.
Logo in files along with some examples of websites that we like. Please ask if any further info needed.
Menu should have:
About
New Patients
Treatments
Fees
Contact Us

Industry/Entity Type

Dentistry

Number of Pages Required

4 page

Font styles to use
Sans Serif

Colors

Designer to choose colors to be used in the design.

Requirements
Must have
• zorvex reviews badge, book online button,
Nice to have
• neutral, relaxing colours
Should not have
• harsh, bright colours!

```html
<!DOCTYPE html>
<html lang="en">
<head>
<meta charset="utf-8">
<title>Brindle Dental Practice</title>
<link rel="stylesheet" href="https://fonts.googleapis.com/css2?family=Ubuntu:wght@500;700&family=Open+Sans:wght@400;600;700&display=swap">
<style>
:root{
  --espresso:#3d322c;
  --espresso-deep:#2c2420;
  --tan:#a8866a;
  --tan-soft:#cdb7a2;
  --paper:#f7f3ee;
  --white:#ffffff;
  --text:#7a716a;
  --ink:#2b2522;
  --accent:#c9743f;
  --field:#54473f;
  --star:#d9a441;
}
*{margin:0;padding:0;box-sizing:border-box}
html,body{width:1200px;height:4183px;overflow:hidden}
body{position:relative;background:var(--white);font-family:"Open Sans",Arial,sans-serif;color:var(--ink)}
.abs{position:absolute}
.head{font-family:"Ubuntu","Open Sans",sans-serif;font-weight:500;color:var(--espresso)}
.eyebrow{font-size:13px;font-weight:600;color:var(--tan);text-decoration:underline;text-underline-offset:4px;letter-spacing:.3px}
.section-title{font-size:42px;text-align:center;width:1200px;left:0}
.btn{display:flex;align-items:center;justify-content:center;gap:14px;background:var(--tan);color:var(--white);font-weight:700;border-radius:3px}

/* top bar & header */
.topbar{left:0;top:0;width:1200px;height:54px;background:var(--paper)}
.updates{left:264px;top:17px;font-size:12px;color:var(--ink);display:flex;align-items:center;gap:10px}
.updates b{color:var(--accent)}
.header{left:0;top:54px;width:1200px;height:66px;background:var(--white)}
.logo-box{left:0;top:0;width:220px;height:120px;background:var(--white);display:flex;align-items:center;justify-content:center;gap:10px}
.logo-mark{width:22px;height:22px;border:2px solid var(--tan-soft)}
.logo-name{font-size:15px;font-weight:600;color:var(--tan);line-height:1.25}
.nav{left:248px;top:79px;font-size:11px;font-weight:700;color:var(--ink)}
.nav span{position:absolute;white-space:nowrap}
.enquiry-icon{left:966px;top:63px;width:48px;height:48px;border-radius:50%;background:#4f4641}
.enquiry{left:1028px;top:67px;font-size:11px;line-height:1.7}
.enquiry small{color:var(--tan);font-weight:700;font-size:10px}
.enquiry strong{display:block;font-size:14px;color:var(--ink)}

/* hero */
.hero{left:0;top:120px;width:1200px;height:710px;background:linear-gradient(90deg,#3a2f29 0%,#5a4a40 35%,#9c8a7c 65%,#d9d0c6 100%)}
.hero-title{left:114px;top:305px;font-size:42px;line-height:47px;color:var(--white);font-weight:700;font-family:"Open Sans",sans-serif}
.hero-text{left:114px;top:424px;width:410px;font-size:18px;line-height:27px;color:var(--white);font-weight:600}
.hero-btn{left:114px;top:529px;width:144px;height:40px;border-radius:20px;font-size:12px}

/* about */
.about{left:0;top:828px;width:1200px;height:564px;background:var(--paper)}
.about-photo{left:102px;top:897px;width:440px;height:440px;border-radius:50%;background:radial-gradient(circle at 45% 45%,#f4eee8,#cbb9a8 60%,#8a7262)}
.about-ring{left:96px;top:897px;width:446px;height:446px;border-radius:50%;border-left:14px solid #6b5a4f;border-top:8px solid #6b5a4f}
.spinner{left:435px;top:1226px;width:98px;height:98px;border-radius:50%;background:var(--white);box-shadow:0 4px 14px rgba(0,0,0,.12)}
.about-text{left:617px;top:906px;width:510px}
.about-text h2{font-size:42px;line-height:53px;margin-top:14px}
.about-text h3{font-family:"Ubuntu",sans-serif;font-weight:500;font-size:23px;color:var(--espresso);margin-top:18px}
.about-text p{font-size:12.5px;line-height:22px;color:var(--text);margin-top:14px}
.about-btn{left:619px;top:1275px;width:154px;height:44px;font-size:15px}

/* services */
.card{top:1605px;width:321px;height:342px;overflow:hidden}
.card-photo{position:absolute;inset:0}
.card-bar{position:absolute;left:0;bottom:0;width:100%;height:46px;background:rgba(61,50,44,.88);color:var(--white);text-align:center;font-family:"Ubuntu",sans-serif;font-weight:700;font-size:19px;line-height:46px}
.card-icon{position:absolute;left:50%;bottom:28px;transform:translateX(-50%);width:50px;height:50px;border-radius:50%;background:rgba(61,50,44,.88);display:flex;align-items:center;justify-content:center}
.card-open{position:absolute;inset:0;background:rgba(61,50,44,.75);color:var(--white);text-align:center;padding:100px 40px 0}
.card-open h4{font-family:"Ubuntu",sans-serif;font-weight:700;font-size:19px;margin-top:14px}
.card-open p{font-size:13.5px;line-height:21px;margin-top:16px}

/* help */
.help{left:0;top:2025px;width:1200px;height:422px;background:var(--espresso)}
.help-photo{left:690px;top:2025px;width:510px;height:422px;background:linear-gradient(120deg,#4a3d35,#8a7565 45%,#d8cbbd 80%,#8d7a6c)}
.help-title{left:100px;top:2098px;font-size:52px;line-height:64px;color:var(--white);font-weight:700}
.help-text{left:100px;top:2240px;font-size:23px;line-height:34px;color:var(--white)}
.help-btn{left:106px;top:2339px;width:155px;height:44px;font-size:16px}

/* reviews */
.reviews{left:0;top:2447px;width:1200px;height:569px;background:var(--paper)}
.review{top:2644px;width:318px;height:182px;background:var(--white);border-radius:6px;box-shadow:0 4px 18px rgba(60,40,30,.08);padding:33px 20px 0 22px;font-size:15px;line-height:23px;color:var(--text)}
.review.active{background:var(--tan);color:var(--white)}
.tail{top:2826px;width:0;height:0;border-top:20px solid var(--tan);border-right:20px solid transparent}
.avatar{top:2861px;width:46px;height:46px;border-radius:50%;background:linear-gradient(#e4dcd4,#a99889)}
.reviewer{top:2862px;font-size:15px;font-weight:700;color:var(--ink);line-height:22px}
.reviewer small{display:block;font-size:12px;font-weight:400;color:var(--text)}
.reviewer.active{color:var(--tan)}
.dots{left:565px;top:2959px;display:flex;gap:5px;align-items:center}
.dots i{width:8px;height:8px;border-radius:50%;background:var(--tan-soft);display:block}
.dots i:first-child{width:22px;border-radius:4px;background:var(--espresso)}
.rating{left:935px;top:2538px;width:170px;height:50px;background:var(--white);border-radius:25px;box-shadow:0 4px 14px rgba(60,40,30,.08);display:flex;align-items:center;gap:10px;padding:0 16px}
.rating-dot{width:22px;height:22px;border-radius:50%;background:var(--tan)}
.rating-name{font-size:12px;font-weight:700;color:var(--espresso);line-height:15px}
.rating-stars{display:flex;gap:2px;margin-top:2px}

/* contact */
.form{left:112px;top:3266px;width:484px;height:360px;background:var(--espresso)}
.form h3{position:absolute;left:50px;top:28px;font-family:"Ubuntu",sans-serif;font-size:24px;color:var(--white);font-weight:700;display:flex;align-items:center;gap:32px}
.form h3::after{content:"";width:46px;height:2px;background:var(--tan)}
.field{position:absolute;background:var(--field);border-bottom:2px solid var(--tan);color:var(--white);font-size:11.5px;padding:0 18px;display:flex;align-items:center;justify-content:space-between}
.book-btn{left:162px;top:3555px;width:124px;height:37px;font-size:11.5px;gap:6px}
.contact-photo{left:596px;top:3282px;width:484px;height:330px;background:linear-gradient(120deg,#efe9e2,#cdbba9 45%,#8d7463 85%)}

/* footer */
.footer{left:0;top:3800px;width:1200px;height:383px;background:linear-gradient(180deg,#342b26,#241e1a)}
.footer-logo{left:143px;top:3893px;width:174px;height:125px;display:flex;align-items:center;justify-content:center;gap:10px}
.footer-logo .logo-name{color:#ddd0c3;font-size:18px}
.footer-logo .logo-mark{border-color:#ddd0c3}
.footer-sep{top:3945px;width:1px;height:50px;background:#7c6f66}
.info{top:3949px;display:flex;gap:12px;align-items:center;font-size:14px;line-height:19px;color:var(--white)}
.footer-line{left:257px;top:4036px;width:708px;height:1px;background:#7c6f66}
.footer-nav{top:4052px;font-size:15px;color:var(--white)}
.copy{left:146px;top:4130px;font-size:12px;color:var(--white)}
.social{top:4112px;width:26px;height:26px;border:1px solid var(--white);border-radius:3px}
</style>
</head>
<body>

<!-- Top bar & header -->
<div class="abs topbar"></div>
<div class="abs updates">
  <svg width="14" height="12" viewBox="0 0 14 12"><rect x=".5" y=".5" width="13" height="11" fill="none" stroke="#cdb7a2"/><path d="M3 4h8M3 7h6" stroke="#cdb7a2"/></svg>
  <span><b>UPDATES:</b>&nbsp; Lorem ipsum dolor sit amet, consectetur adipiscing elit, sed do eiusmod tempor incididunt ut labore et dolore magna aliqua.</span>
</div>
<div class="abs header"></div>
<div class="abs logo-box"><span class="logo-mark"></span><span class="logo-name">Brindle<br>Dental Practice</span></div>
<nav class="abs nav">
  <span style="left:0;color:#a8866a">HOME</span>
  <span style="left:75px">ABOUT US</span>
  <span style="left:168px">TREATMENTS</span>
  <span style="left:275px">NEW PATIENTS</span>
  <span style="left:393px">FEES</span>
  <span style="left:452px">CONTACT US</span>
</nav>
<div class="abs enquiry-icon">
  <svg width="48" height="48" viewBox="0 0 48 48"><path d="M18 15c2-1 3 0 4 2l1 3c0 1-1 2-2 3 1 3 3 5 6 6 1-1 2-2 3-2l3 1c2 1 3 2 2 4-1 2-3 3-5 3-8-1-14-7-15-15 0-2 1-4 3-5z" fill="#fff"/></svg>
</div>
<div class="abs enquiry"><small>ENQURIES</small><strong>+ 1-888-555-01-234</strong></div>

<!-- Hero -->
<section class="abs hero" role="img" aria-label="Dentist examining a smiling senior patient in the chair"></section>
<svg class="abs" style="left:0;top:720px" width="1200" height="115" viewBox="0 0 1200 115">
  <path d="M0 80 C300 20 600 0 850 70 C1000 110 1120 80 1200 50 L1200 115 L0 115Z" fill="#f7f3ee"/>
  <path d="M0 80 C250 30 500 20 700 50 C850 75 950 100 1050 95 C1120 90 1170 70 1200 50 C1150 90 1050 110 950 105 C800 95 600 40 350 50 C200 55 80 70 0 80Z" fill="#a8866a"/>
</svg>
<h1 class="abs hero-title">Precision Dentistry,<br>Personal Touch</h1>
<p class="abs hero-text">Lorem ipsum dolor sit amet, consectetur adip iscing elit, sed do eiusmod tempor incididunt ut labore et dolore</p>
<a class="abs btn hero-btn">READ MORE</a>

<!-- About -->
<section class="abs about"></section>
<div class="abs about-ring"></div>
<div class="abs about-photo" role="img" aria-label="Dentist treating a smiling female patient"></div>
<div class="abs spinner">
  <svg width="98" height="98" viewBox="0 0 98 98"><g stroke="#a8866a" stroke-width="3.5" stroke-linecap="round">
    <path d="M49 30v8M49 60v8M30 49h8M60 49h8M36 36l5 5M57 57l5 5M62 36l-5 5M41 57l-5 5"/></g></svg>
</div>
<div class="abs about-text">
  <span class="eyebrow">WHO WE ARE</span>
  <h2 class="head">The team you can trust<br>to get the job done</h2>
  <h3>Brightening Smiles, One Tooth at a Time</h3>
  <p>Lorem ipsum dolor sit amet, consectetur adipiscing elit, sed do eiusmod tempor incididunt ut labore et dolore magna aliqua. Ut enim ad minim veniam, quis nos trud exercitation ullamco laboris nisi ut aliquip ex ea commodo consequat. Duis aute irure dolor in reprehenderit in voluptate velit esse cillum dolore eu fugiat nulla pariatur. Excepteur sint occaecat cupidatat non proident, sunt in culpa qui officia deserunt mollit anim id est laborum.</p>
</div>
<a class="abs btn about-btn">Contact us
  <svg width="18" height="14" viewBox="0 0 18 14"><path d="M1 7h15M10 1l6 6-6 6" fill="none" stroke="#fff" stroke-width="2"/></svg></a>

<!-- Services -->
<span class="abs eyebrow" style="left:0;width:1200px;text-align:center;top:1466px">OUR SERVICES</span>
<h2 class="abs head section-title" style="top:1502px">Services We Offer</h2>

<div class="abs card" style="left:93px">
  <div class="card-photo" role="img" aria-label="Smiling young girl at the dentist" style="background:linear-gradient(135deg,#6e5a4d,#e2d8ce 55%,#b39f8e)"></div>
  <div class="card-bar">General Dentistry</div>
  <div class="card-icon"><svg width="26" height="26" viewBox="0 0 26 26"><path d="M13 3l9 6-3 11H7L4 9z" fill="none" stroke="#fff" stroke-width="1.8"/></svg></div>
</div>
<div class="abs card" style="left:438px">
  <div class="card-photo" role="img" aria-label="Woman checking her smile in a mirror" style="background:linear-gradient(135deg,#9c8d80,#d8c3b3 60%,#7c6a5d)"></div>
  <div class="card-open">
    <svg width="70" height="70" viewBox="0 0 70 70"><path d="M35 8l24 16-8 30H19L11 24z" fill="none" stroke="#fff" stroke-width="3"/><g fill="#fff"><circle cx="35" cy="8" r="5"/><circle cx="59" cy="24" r="5"/><circle cx="51" cy="54" r="5"/><circle cx="19" cy="54" r="5"/><circle cx="11" cy="24" r="5"/></g></svg>
    <h4>Cosmetic Dentistry</h4>
    <p>Lorem ipsum dolor sit amet, conse ctetur adipiscing elit, sed do eius mod tempor incididunt ut labore et dolore magna aliqua.</p>
  </div>
</div>
<div class="abs card" style="left:788px">
  <div class="card-photo" role="img" aria-label="Smiling senior man during a dental check" style="background:linear-gradient(135deg,#ddd3ca,#f0ebe6 50%,#a08b7b)"></div>
  <div class="card-bar">Orthodontics</div>
  <div class="card-icon"><svg width="26" height="26" viewBox="0 0 26 26"><path d="M13 3l9 6-3 11H7L4 9z" fill="none" stroke="#fff" stroke-width="1.8"/></svg></div>
</div>

<!-- Help -->
<section class="abs help"></section>
<div class="abs help-photo" role="img" aria-label="Doctor and nurse in masks reviewing a clipboard"></div>
<h2 class="abs help-title">NEED HELP? WE'RE<br>AVAILABLE 24/7</h2>
<p class="abs help-text">Call Us or submit a form below to speak with<br>an expert today for a free quote</p>
<a class="abs btn help-btn">Contact us
  <svg width="18" height="14" viewBox="0 0 18 14"><path d="M1 7h15M10 1l6 6-6 6" fill="none" stroke="#fff" stroke-width="2"/></svg></a>

<!-- Reviews -->
<section class="abs reviews"></section>
<span class="abs eyebrow" style="left:0;width:1200px;text-align:center;top:2492px">TESTIMONIALS</span>
<h2 class="abs head section-title" style="top:2528px">Clients' Reviews</h2>

<div class="abs rating" aria-label="zorvex reviews rating 4.9 out of 5">
  <span class="rating-dot"></span>
  <div>
    <div class="rating-name">zorvex reviews 4.9</div>
    <div class="rating-stars">
      <svg width="12" height="12" viewBox="0 0 12 12"><path d="M6 .5l1.6 3.5 3.9.4-2.9 2.6.8 3.8L6 8.9 2.6 10.8l.8-3.8L.5 4.4l3.9-.4z" fill="#d9a441"/></svg>
      <svg width="12" height="12" viewBox="0 0 12 12"><path d="M6 .5l1.6 3.5 3.9.4-2.9 2.6.8 3.8L6 8.9 2.6 10.8l.8-3.8L.5 4.4l3.9-.4z" fill="#d9a441"/></svg>
      <svg width="12" height="12" viewBox="0 0 12 12"><path d="M6 .5l1.6 3.5 3.9.4-2.9 2.6.8 3.8L6 8.9 2.6 10.8l.8-3.8L.5 4.4l3.9-.4z" fill="#d9a441"/></svg>
      <svg width="12" height="12" viewBox="0 0 12 12"><path d="M6 .5l1.6 3.5 3.9.4-2.9 2.6.8 3.8L6 8.9 2.6 10.8l.8-3.8L.5 4.4l3.9-.4z" fill="#d9a441"/></svg>
      <svg width="12" height="12" viewBox="0 0 12 12"><path d="M6 .5l1.6 3.5 3.9.4-2.9 2.6.8 3.8L6 8.9 2.6 10.8l.8-3.8L.5 4.4l3.9-.4z" fill="#d9a441"/></svg>
    </div>
  </div>
</div>

<div class="abs review" style="left:93px">Lorem ipsum dolor sit amet, consectetur adipiscing elit, sed do eiusmod tempor incididunt ut labore et dolore magna aliqua. Ut enim ad minim veniam.</div>
<div class="abs review active" style="left:438px">Lorem ipsum dolor sit amet, consectetur adipiscing elit, sed do eiusmod tempor incididunt ut labore et dolore magna aliqua. Ut enim ad minim veniam.</div>
<div class="abs review" style="left:784px">Lorem ipsum dolor sit amet, consectetur adipiscing elit, sed do eiusmod tempor incididunt ut labore et dolore magna aliqua. Ut enim ad minim veniam.</div>
<div class="abs tail" style="left:93px"></div>
<div class="abs tail" style="left:438px"></div>
<div class="abs tail" style="left:784px"></div>

<div class="abs avatar" style="left:114px" role="img" aria-label="Reviewer portrait"></div>
<div class="abs reviewer" style="left:192px">Tomas Reyes<small>Engineer</small></div>
<div class="abs avatar" style="left:460px;background:linear-gradient(#f1e3b8,#d9a93c)" role="img" aria-label="Reviewer portrait"></div>
<div class="abs reviewer active" style="left:537px">Tomas Reyes<small>Engineer</small></div>
<div class="abs avatar" style="left:805px" role="img" aria-label="Reviewer portrait"></div>
<div class="abs reviewer" style="left:882px">Tomas Reyes<small>Engineer</small></div>
<div class="abs dots"><i></i><i></i><i></i><i></i></div>

<!-- Contact -->
<span class="abs eyebrow" style="left:0;width:1200px;text-align:center;top:3095px">CONTACT US</span>
<h2 class="abs head section-title" style="top:3130px">Get un Touch with Us</h2>

<div class="abs form"><h3>Get in touch</h3></div>
<div class="field" style="left:162px;top:3342px;width:184px;height:36px">Your name*</div>
<div class="field" style="left:362px;top:3342px;width:184px;height:36px">Phone number...</div>
<div class="field" style="left:162px;top:3393px;width:384px;height:35px">Choose Service*
  <svg width="10" height="6" viewBox="0 0 10 6"><path d="M1 1l4 4 4-4" fill="none" stroke="#fff" stroke-width="1.4"/></svg></div>
<div class="field" style="left:162px;top:3443px;width:384px;height:99px;align-items:flex-start;padding-top:14px">Message...</div>
<a class="abs btn book-btn">
  <svg width="12" height="12" viewBox="0 0 12 12"><path d="M11 1L1 5l4 2 2 4z" fill="none" stroke="#fff" stroke-width="1.2"/></svg>Book Online</a>
<div class="abs contact-photo" role="img" aria-label="Smiling dental team with a patient"></div>

<!-- Footer -->
<svg class="abs" style="left:0;top:3695px" width="1200" height="110" viewBox="0 0 1200 110">
  <rect width="1200" height="110" fill="#ffffff"/>
  <path d="M0 60 C200 10 450 20 650 55 C850 90 1050 70 1200 25 L1200 110 L0 110Z" fill="#342b26"/>
  <path d="M0 60 C200 10 450 10 650 40 C850 70 1050 60 1180 20 C1060 70 860 90 650 65 C450 40 200 30 0 60Z" fill="#a8866a"/>
</svg>
<footer class="abs footer"></footer>
<div class="abs footer-logo"><span class="logo-mark"></span><span class="logo-name">Brindle<br>Dental Practice</span></div>

<div class="abs footer-sep" style="left:412px"></div>
<div class="abs info" style="left:432px">
  <svg width="30" height="30" viewBox="0 0 30 30"><g fill="none" stroke="#fff" stroke-width="1.4"><circle cx="15" cy="15" r="13"/><ellipse cx="15" cy="15" rx="6" ry="13"/><path d="M2 15h26M4 8h22M4 22h22"/></g></svg>
  <span>123, Building Name, Street<br>City, State XY 123456</span>
</div>
<div class="abs footer-sep" style="left:668px"></div>
<div class="abs info" style="left:688px">
  <svg width="30" height="30" viewBox="0 0 30 30"><g fill="none" stroke="#fff" stroke-width="1.4"><rect x="7" y="3" width="14" height="24" rx="2"/><path d="M12 23h4M24 11c2 2 2 6 0 8"/></g></svg>
  <span>PHONE<br>(123) 456 7890</span>
</div>
<div class="abs footer-sep" style="left:847px"></div>
<div class="abs info" style="left:866px">
  <svg width="30" height="30" viewBox="0 0 30 30"><g fill="none" stroke="#fff" stroke-width="1.4"><rect x="3" y="8" width="24" height="17"/><path d="M3 8l12 9 12-9"/></g></svg>
  <span>EMAIL<br>info@company.com</span>
</div>

<div class="abs footer-line"></div>
<span class="abs footer-nav" style="left:276px">HOME</span>
<span class="abs footer-nav" style="left:369px">SERVICES</span>
<span class="abs footer-nav" style="left:475px">ABOUT US</span>
<span class="abs footer-nav" style="left:594px">TESTIMONIALS</span>
<span class="abs footer-nav" style="left:746px">BLOG</span>
<span class="abs footer-nav" style="left:837px">CONTACT US</span>

<span class="abs copy">Brindle Dental Practice</span>
<span class="abs social" style="left:934px" aria-label="Social profile"></span>
<span class="abs social" style="left:967px" aria-label="Social profile"></span>
<span class="abs social" style="left:1000px" aria-label="Social profile"></span>
<span class="abs social" style="left:1033px" aria-label="Social profile"></span>

</body>
</html>
```